Website redesign - valmoxy.com

We are looking to do a full redesign of valmoxy.com. Need a designer to come up overall layout and 3 specific pages and 3 different hero images.
Wireframes for the 3 pages are attached as well as site images. You don't have to follow the wireframes exactly, but instead the wireframe is there to show you the information that needs to be on each page. Feel free to rearrange as needed.
Our target market is self taught engineers. So definitely I want a more casual feel to it. I'm ok with fun bold colors as well. Really like websites that have the infinite scroll look/feel to them.
Looking to find a designer who will produce HTML and potentially even implement the HTML into our site checked in code.
HTML Code should be responsive/mobile first leveraging Bootstrap 4.
Attached files include:
0) Wireframe PDF
https://files.plimtree.net/share/8Kq2Lw7Zr4Tn9Vb3Xc6Md1Hs5Fy0Pj/view?ref=link
1) Valmoxy Images zip 1
https://files.plimtree.net/share/4Rt8Gm2Yk6Wd1Ne9Sb5Qh3Lx7Cv0Uz/view?ref=link
2) Valmoxy Images zip 2
https://files.plimtree.net/share/2Ja5Pf9Ko3Ex8Ti1Mr6Wg4Dn0Bs7Qy/view?ref=link
I sell DIY Waterproof Electronics enclosures. Target audience is self taught DIY engineers
Coded - Design and coding required
3 page
Designer to choose colors to be used in the design.

```html
<!DOCTYPE html>
<html lang="en">
<head>
<meta charset="utf-8">
<title>Valmoxy – Enclosures</title>
<link href="https://fonts.googleapis.com/css2?family=Lato:wght@300;400;700;900&display=swap" rel="stylesheet">
<style>
:root{
  --brand-blue:#0a1cf2;
  --logo-blue:#1a1fd6;
  --accent-lime:#d4dc00;
  --ink:#222;
  --muted:#8a8a8a;
  --card-bg:#f7f7f7;
  --photo-bg:#ffffff;
}
*{box-sizing:border-box;margin:0;padding:0}
html,body{width:1200px;height:2212px;overflow:hidden}
body{position:relative;font-family:'Lato',sans-serif;color:var(--ink);background:#fff}
.site-header{position:absolute;top:0;left:0;width:1200px;height:159px;background:linear-gradient(180deg,#f1f1f1 0%,#e9e9e9 60%,#e2e2e2 100%)}
.brand{position:absolute;display:flex;align-items:center;gap:8px;font-weight:700;color:var(--logo-blue);letter-spacing:1px}
.brand-dot{width:14px;height:14px;border-radius:50%;background:var(--accent-lime)}
.site-header .brand{left:89px;top:38px;font-size:48px}
.main-nav{position:absolute;left:468px;top:50px;display:flex;gap:29px;font-size:14px;color:#333}
.btn{position:absolute;top:45px;width:104px;height:34px;font-size:14px;display:flex;align-items:center;justify-content:center}
.btn-outline{left:885px;border:2px solid var(--logo-blue);color:var(--logo-blue)}
.btn-solid{left:1007px;background:var(--accent-lime);color:#fff}
.page-title{position:absolute;top:220px;left:0;width:1200px;text-align:center;font-size:44px;font-weight:700;line-height:48px}
.section-title{position:absolute;left:89px;font-size:44px;font-weight:700}
.card-row{position:absolute;left:89px;display:flex;gap:9px}
.card{width:197px;height:300px;background:var(--card-bg);box-shadow:0 1px 5px rgba(0,0,0,.12)}
.card-photo{height:143px;background:linear-gradient(160deg,#fafafa,#d9d9d9)}
.photo-board{background:linear-gradient(160deg,#eef0ea,#6f7b63 60%,#3b3b3b)}
.photo-wood{background:linear-gradient(160deg,#f3ebdd,#c9a676)}
.photo-crate-brown{background:linear-gradient(160deg,#f3f0ec,#7d6b5b)}
.photo-crate-green{background:linear-gradient(160deg,#f1f3ee,#6a7358)}
.photo-clear{background:linear-gradient(160deg,#faf8ff,#d8d3ec)}
.card-body{padding:10px 11px}
.spec-label{font-size:14px;line-height:18px}
.spec-value{font-size:9px;line-height:14px;color:var(--muted);padding-left:1px}
.spec-gap{height:28px}
.site-footer{position:absolute;top:2033px;left:0;width:1200px;height:179px;background:var(--brand-blue);color:#fff}
.site-footer .brand{left:91px;top:64px;font-size:44px;color:#fff}
.stay-title{position:absolute;left:928px;top:46px;font-size:20px;font-weight:700;color:#fff}
.social{position:absolute;top:92px;left:880px;display:flex;align-items:center;gap:12px;font-size:13px}
.social-icon{width:26px;height:26px;border-radius:50%;background:rgba(255,255,255,.2)}
.divider{margin:0 18px}
.footer-rule{position:absolute;left:89px;top:125px;width:1022px;height:1px;background:rgba(255,255,255,.25)}
.copyright{position:absolute;top:145px;width:1200px;text-align:center;font-size:14px}
.chat-bubble{position:absolute;left:1135px;top:2137px;width:43px;height:43px;border-radius:50%;background:#fff;display:flex;align-items:center;justify-content:center;box-shadow:0 2px 6px rgba(0,0,0,.2)}
</style>
</head>
<body>
<header class="site-header">
  <div class="brand"><span class="brand-dot"></span>valmoxy</div>
  <nav class="main-nav"><span>Get Started</span><span>Designs</span><span>FAQs</span><span>Videos</span><span>Contact Us</span></nav>
  <a class="btn btn-outline">Sign Up</a>
  <a class="btn btn-solid">Sign Up</a>
</header>

<h1 class="page-title">Valmoxy Premium GrowCase<br>Enclosures</h1>

<div class="card-row" style="top:344px">
  <div class="card"><div class="card-photo" role="img" aria-label="Grey hinged enclosure box"></div><div class="card-body"><p class="spec-label">Power Options</p><p class="spec-value">4x - Brightwell 350w</p><p class="spec-value">2x - NX Common Slot - 1200w</p><p class="spec-label">Component Space</p><p class="spec-value">Double Decker</p><p class="spec-value">127sq real estate</p><p class="spec-label">Enclosure Size</p><p class="spec-value">27in x 14in x 7in (height)</p></div></div>
  <div class="card"><div class="card-photo photo-board" role="img" aria-label="Two-tier circuit board assembly"></div><div class="card-body"><p class="spec-label">Power Options</p><p class="spec-value">4x - Brightwell 350w</p><p class="spec-value">2x - NX Common Slot - 1200w</p><p class="spec-label">Component Space</p><p class="spec-value">Double Decker</p><p class="spec-value">127sq real estate</p><p class="spec-label">Enclosure Size</p><p class="spec-value">27in x 14in x 7in (height)</p></div></div>
  <div class="card"><div class="card-photo photo-board" role="img" aria-label="Mounted circuit boards on tray"></div><div class="card-body"><p class="spec-label">Power Options</p><p class="spec-value">4x - Brightwell 350w</p><p class="spec-value">2x - NX Common Slot - 1200w</p><p class="spec-label">Component Space</p><p class="spec-value">Double Decker</p><p class="spec-value">127sq real estate</p><p class="spec-label">Enclosure Size</p><p class="spec-value">27in x 14in x 7in (height)</p></div></div>
  <div class="card"><div class="card-photo photo-wood" role="img" aria-label="Flat-pack panel kit with hardware"></div><div class="card-body"><p class="spec-label">Power Options</p><p class="spec-value">4x - Brightwell 350w</p><p class="spec-value">2x - NX Common Slot - 1200w</p><p class="spec-label">Component Space</p><p class="spec-value">Double Decker</p><p class="spec-value">127sq real estate</p><p class="spec-label">Enclosure Size</p><p class="spec-value">27in x 14in x 7in (height)</p></div></div>
  <div class="card"><div class="card-photo photo-board" role="img" aria-label="Stacked board rack assembly"></div><div class="card-body"><p class="spec-label">Power Options</p><p class="spec-value">4x - Brightwell 350w</p><p class="spec-value">2x - NX Common Slot - 1200w</p><p class="spec-label">Component Space</p><p class="spec-value">Double Decker</p><p class="spec-value">127sq real estate</p><p class="spec-label">Enclosure Size</p><p class="spec-value">27in x 14in x 7in (height)</p></div></div>
</div>

<h2 class="section-title" style="top:706px">RTK Ammo Crates</h2>
<div class="card-row" style="top:784px;left:90px">
  <div class="card"><div class="card-photo photo-crate-brown" role="img" aria-label="Brown plastic crate"></div><div class="card-body"><p class="spec-label">Power Options</p><p class="spec-value">4x - Brightwell 350w</p><p class="spec-value">2x - NX Common Slot - 1200w</p><p class="spec-label">Component Space</p><div class="spec-gap"></div><p class="spec-label">Enclosure Size</p><p class="spec-value">27in x 14in x 7in (height)</p></div></div>
  <div class="card"><div class="card-photo photo-crate-green" role="img" aria-label="Green plastic crate"></div><div class="card-body"><p class="spec-label">Power Options</p><p class="spec-value">4x - Brightwell 350w</p><p class="spec-value">2x - NX Common Slot - 1200w</p><p class="spec-label">Component Space</p><p class="spec-value">Double Decker</p><p class="spec-value">127sq real estate</p><p class="spec-label">Enclosure Size</p><p class="spec-value">27in x 14in x 7in (height)</p></div></div>
  <div class="card"><div class="card-photo" role="img" aria-label="Grey weatherproof box"></div><div class="card-body"><p class="spec-label">Power Options</p><p class="spec-value">4x - Brightwell 350w</p><p class="spec-value">2x - NX Common Slot - 1200w</p><p class="spec-label">Component Space</p><p class="spec-value">Double Decker</p><p class="spec-value">127sq real estate</p><p class="spec-label">Enclosure Size</p><p class="spec-value">27in x 14in x 7in (height)</p></div></div>
</div>

<h2 class="section-title" style="top:1146px">Cable Guard (CG) Enclosures</h2>
<div class="card-row" style="top:1222px;left:90px">
  <div class="card"><div class="card-photo photo-clear" role="img" aria-label="Clear ribbed cable guard box"></div><div class="card-body"><p class="spec-label">Power Options</p><p class="spec-value">4x - Brightwell 350w</p><p class="spec-value">2x - NX Common Slot - 1200w</p><p class="spec-label">Component Space</p><div class="spec-gap"></div><p class="spec-label">Enclosure Size</p><p class="spec-value">27in x 14in x 7in (height)</p></div></div>
  <div class="card"><div class="card-photo photo-clear" role="img" aria-label="Tall clear cable guard box"></div><div class="card-body"><p class="spec-label">Power Options</p><p class="spec-value">4x - Brightwell 350w</p><p class="spec-value">2x - NX Common Slot - 1200w</p><p class="spec-label">Component Space</p><p class="spec-value">Double Decker</p><p class="spec-value">127sq real estate</p><p class="spec-label">Enclosure Size</p><p class="spec-value">27in x 14in x 7in (height)</p></div></div>
</div>

<h2 class="section-title" style="top:1586px">Specialty Enclosures</h2>
<div class="card-row" style="top:1662px;left:90px">
  <div class="card"><div class="card-photo photo-wood" role="img" aria-label="Panel kit with bag of fasteners"></div><div class="card-body"><p class="spec-label">Power Options</p><p class="spec-value">4x - Brightwell 350w</p><p class="spec-value">2x - NX Common Slot - 1200w</p><p class="spec-label">Component Space</p><div class="spec-gap"></div><p class="spec-label">Enclosure Size</p><p class="spec-value">27in x 14in x 7in (height)</p></div></div>
</div>

<footer class="site-footer">
  <div class="brand"><span class="brand-dot" style="background:#fff"></span>valmoxy</div>
  <p class="stay-title">Stay Connected</p>
  <div class="social"><span class="social-icon"></span><span>Vidcast</span><span class="divider">|</span><span class="social-icon"></span><span>Friendboard</span></div>
  <div class="footer-rule"></div>
  <p class="copyright">Copyright 2020 @ valmoxy designer.</p>
</footer>
<div class="chat-bubble"><svg width="22" height="22" viewBox="0 0 22 22"><path d="M11 2a8 8 0 1 1-4.5 14.6L3 18l1.3-3.6A8 8 0 0 1 11 2z" fill="#9acd32"/></svg></div>
</body>
</html>
```